Pet sitting Business needs a website

We need a website that shows our services and prices. Shows our love of animals but also our professionalism. want a gallery, about, blog, services, links to fb and instagram accounts, newsletter archive. want it to be easy to access and wonderful to navigate. want the domain to be Birchvalecritterden.com
take any info from FB site www.facebook.com/birchvalecritterden
I would like it to fit tidy frame platform

Target Market(s)

upscale area, responsible pet owners,

Industry/Entity Type

Pet Care

Coding

Coded - Design and coding required

Number of Pages Required

5+ page

Font styles to use
Sans Serif

Requirements
Must have
• (tidy frame platform)
• Menu
• photo gallery
• about us
• services
• policies
• monthly newsletter
• unavailable dates
• Introduction (welcome)
• payment methods
• Daily updates
• testimonials (use from fb site)
Should not have
• stock photos

```html
<!DOCTYPE html>
<html lang="en">
<head>
<meta charset="utf-8">
<title>Birchvale Critter Den – Pet Sitting</title>
<link rel="stylesheet" href="https://fonts.googleapis.com/css2?family=Roboto:ital,wght@0,400;0,500;0,700;1,400&family=Caveat:wght@500&display=swap">
<style>
:root{
  --blue:#1f72a8;
  --blue-dark:#1a6596;
  --sky-a:#2d8ccb;
  --sky-b:#5dbdec;
  --gold:#e4a21c;
  --gold-line:#e2b45a;
  --ink:#222;
  --grey:#666;
  --white:#fff;
  --hero-a:#8a6a35;
  --hero-b:#c8a35e;
}
*{box-sizing:border-box;margin:0;padding:0}
html,body{width:1200px;height:2410px;overflow:hidden}
body{position:relative;background:var(--white);font-family:"Roboto",Arial,sans-serif;color:var(--ink)}
.abs{position:absolute}

/* top bar */
.topbar{top:0;left:0;width:1200px;height:35px;background:var(--white);font-size:13px;color:#777}
.topbar .item{top:9px;display:flex;align-items:center;gap:6px}
.reserve{top:7px;left:941px;width:135px;height:21px;background:var(--gold);color:var(--white);font-size:12.5px;font-weight:500;text-align:center;line-height:21px;border-radius:3px}
.social-dot{top:12px;width:11px;height:11px;border-radius:50%;background:#999}

/* nav */
.navband{top:35px;left:0;width:1200px;height:71px;background:var(--blue)}
.logo{top:35px;left:55px;width:284px;height:81px;background:var(--white);border-radius:0 0 8px 8px;box-shadow:0 2px 6px rgba(0,0,0,.15);display:flex;align-items:center;justify-content:center;gap:10px;color:var(--gold);font-size:22px;font-weight:500}
.logo .mark{width:14px;height:14px;border-radius:50%;background:var(--gold)}
.nav a{position:absolute;top:66px;color:var(--white);font-size:15.5px;font-weight:500;text-decoration:none}

/* hero */
.hero{top:106px;left:0;width:1200px;height:482px;background:linear-gradient(100deg,var(--hero-a),var(--hero-b) 55%,#6b4e26)}
.hero-title{top:222px;left:55px;width:480px;font-family:"Caveat",cursive;font-size:66px;line-height:54px;color:var(--white);text-align:center}
.btn-ghost{top:421px;height:34px;background:var(--white);color:var(--blue);font-size:10.5px;font-weight:700;line-height:34px;text-align:center;border-radius:2px}
.dots{top:560px;left:568px;display:flex;gap:6px}
.dots span{width:10px;height:10px;border-radius:50%;background:var(--white)}
.dots span:first-child{background:transparent;border:1.5px solid var(--white)}

/* about */
.about{top:588px;left:0;width:1200px;height:257px;background:linear-gradient(180deg,var(--sky-a),var(--sky-b))}
.about h1{position:absolute;top:600px;left:53px;font-size:27px;font-weight:500;color:var(--white)}
.about-text{top:648px;left:53px;width:720px;font-size:13px;line-height:19.5px;color:var(--white)}
.about-text p+p{margin-top:12px}
.portrait{top:628px;left:820px;width:240px;height:240px;transform:rotate(-6deg);background:var(--gold);padding:10px;box-shadow:0 4px 10px rgba(0,0,0,.3)}
.portrait div{width:100%;height:100%;background:linear-gradient(160deg,#6a4a3a,#2b2520 55%,#4cba3e)}

/* like bar */
.likeline{top:882px;left:64px;width:1071px;height:1px;background:#ddd}
.likepill{top:861px;left:376px;width:450px;height:42px;background:var(--white);border:1px solid #e2e2e2;border-radius:21px;display:flex;align-items:center;font-size:11.5px;color:#444}
.likepill .thumb{width:56px;height:100%;border-right:1px solid #e2e2e2;display:flex;align-items:center;justify-content:center}
.likebtn{margin-left:64px;margin-right:6px;background:#4a6bb0;color:var(--white);font-size:11px;font-weight:700;padding:3px 6px;border-radius:2px}

/* section titles */
.sec-title{left:0;width:1200px;text-align:center;font-size:21px;font-weight:700}
.dotted{left:55px;width:1090px;border-top:2px dotted var(--gold-line)}

/* services */
.card{top:1029px;width:198px;height:151px}
.card .pic{position:absolute;top:0;left:0;width:198px;height:103px}
.card .label{position:absolute;top:97px;left:8px;width:182px;height:54px;background:var(--blue);color:var(--white);font-size:18px;font-weight:500;text-align:center;line-height:54px}
.card .icon{position:absolute;top:-22px;left:77px;width:44px;height:44px;border-radius:50%;background:var(--blue);border:2px solid var(--white);display:flex;align-items:center;justify-content:center}

/* unavailable */
.unavail{top:1200px;left:0;width:1200px;height:273px;background:radial-gradient(ellipse at 60% 80%,var(--sky-b),var(--sky-a) 75%)}
.date{top:1339px;height:46px;border:1.5px solid var(--white);color:var(--white);font-size:19px;font-weight:500;text-align:center;line-height:43px;border-radius:3px}

/* testimonials */
.quote{top:1584px;font-size:12.5px;line-height:19px;font-style:italic;color:var(--grey)}
.quote b{display:block;font-style:normal;font-weight:400;color:var(--ink);margin-top:10px}
.avatar{top:1585px;width:78px;height:78px;border-radius:50%;background:#ccc;font-size:10px;color:#555;display:flex;align-items:center;justify-content:center}
.vdiv{top:1590px;left:599px;width:1px;height:80px;background:#e5e5e5}

/* gallery */
.photo{top:1804px;width:240px;height:175px}

/* footer */
.footer{top:1979px;left:0;width:1200px;height:431px;background:var(--blue-dark)}
.fcol{top:2030px;width:254px;color:var(--white);font-size:13px;line-height:19.5px}
.fcol h3{font-size:18px;font-weight:500;margin-bottom:16px}
.fcol p{margin-bottom:14px}
.field{position:absolute;left:334px;width:252px;background:var(--white);border-radius:2px;color:#999;font-size:12.5px;padding:8px 12px}
.send{top:2244px;left:334px;width:135px;height:32px;background:var(--white);color:var(--ink);font-size:13px;font-weight:500;text-align:center;line-height:32px;border-radius:2px}
.map{top:2070px;left:615px;width:252px;height:211px;background:linear-gradient(135deg,#cfdff0,#e8e4d8 50%,#b9d6a8)}
.fsocial{display:flex;gap:12px;margin-top:4px}
.fsocial span{width:12px;height:12px;border-radius:50%;background:var(--white)}
.fline{top:2346px;left:53px;width:1094px;height:1px;background:rgba(255,255,255,.3)}
.copy{top:2374px;left:0;width:1200px;text-align:center;color:var(--white);font-size:13px}
</style>
</head>
<body>

<!-- top bar -->
<div class="abs topbar">
  <div class="abs item" style="left:557px">
    <svg width="12" height="12" viewBox="0 0 24 24"><path fill="#888" d="M6.6 10.8a15 15 0 0 0 6.6 6.6l2.2-2.2c.3-.3.7-.4 1-.2 1.1.4 2.3.6 3.6.6.6 0 1 .4 1 1V20c0 .6-.4 1-1 1A17 17 0 0 1 3 4c0-.6.4-1 1-1h3.5c.6 0 1 .4 1 1 0 1.3.2 2.5.6 3.6.1.3 0 .7-.2 1z"/></svg>
    555-013-4827
  </div>
  <div class="abs item" style="left:690px">
    <svg width="13" height="10" viewBox="0 0 26 20"><rect x="1" y="1" width="24" height="18" rx="2" fill="#888"/><path d="M2 3l11 8 11-8" stroke="#fff" stroke-width="2" fill="none"/></svg>
    hello@birchvalecritterden.com
  </div>
  <div class="abs reserve">Online Reservations</div>
  <span class="abs social-dot" style="left:1100px"></span>
  <span class="abs social-dot" style="left:1136px"></span>
</div>

<!-- navigation -->
<div class="abs navband"></div>
<div class="abs logo"><span class="mark"></span>Birchvale Critter Den</div>
<nav class="nav">
  <a style="left:504px">HI !</a>
  <a style="left:566px">ABOUT US</a>
  <a style="left:680px">SERVICES</a>
  <a style="left:790px">GALLERY</a>
  <a style="left:895px">BLOG</a>
  <a style="left:973px">POLICIES</a>
  <a style="left:1077px">CONTACT</a>
</nav>

<!-- hero -->
<div class="abs hero" role="img" aria-label="Photo of a terrier resting its head beside a teddy bear"></div>
<div class="abs hero-title">Where Kisses and Hugs are my Speciality</div>
<div class="abs btn-ghost" style="left:146px;width:100px">OUR SERVICES</div>
<div class="abs btn-ghost" style="left:281px;width:106px">GO ON SURFING</div>
<div class="abs dots"><span></span><span></span><span></span><span></span></div>

<!-- about -->
<section class="about abs">
</section>
<h1 class="abs" style="top:600px;left:53px;font-size:27px;font-weight:500;color:var(--white)">Hi my name is Marla Quillfeather</h1>
<div class="abs about-text">
  <p>I would love to introduce myself. I am a Licensed Veterinarian Technician from Millbrook, Ohio. My family and I moved to Birchvale in 2008. I have dedicated the last 13 years to raising my 2 beautiful children and 5 of my furry babies.</p>
  <p>I have the knowledge and the training to give the special care your pet will need. I was a Licensed Veterinarian Technician Supervisor of a major animal hospital in Millbrook. I have spent 20 years of my life taking care of our friends and would to do the same for yours.</p>
</div>
<div class="abs portrait"><div role="img" aria-label="Photo of the pet sitter holding her small dark dog"></div></div>

<!-- like bar -->
<div class="abs likeline"></div>
<div class="abs likepill">
  <div class="thumb"><svg width="18" height="18" viewBox="0 0 24 24"><path fill="#ccc" d="M2 10h4v11H2zM8 21V10l5-8c1.5 0 2.5 1 2 3l-1 4h6c1.2 0 2 1 1.8 2.2l-1.6 7.6c-.2 1.2-1 2.2-2.2 2.2z"/></svg></div>
  <span class="likebtn">✓ Like</span>You and 4.1k others like this.
</div>

<!-- services -->
<div class="abs sec-title" style="top:928px">Our Services</div>
<div class="abs dotted" style="top:967px"></div>

<div class="abs card" style="left:51px">
  <div class="pic" role="img" aria-label="Photo of a shepherd dog in a flower garden" style="background:linear-gradient(135deg,#c2364a,#5c7a2e 60%,#8a6a3c)"></div>
  <div class="label">Daily Visit</div>
  <div class="icon"><svg width="20" height="20" viewBox="0 0 24 24"><path fill="#fff" d="M12 3l9 8h-3v9h-5v-6h-2v6H6v-9H3z"/></svg></div>
</div>
<div class="abs card" style="left:276px">
  <div class="pic" role="img" aria-label="Photo of two small dogs on leashes out for a walk" style="background:linear-gradient(135deg,#8da8c0,#c9c2b8 55%,#6b6f75)"></div>
  <div class="label">Just walks</div>
  <div class="icon"><svg width="20" height="20" viewBox="0 0 24 24"><circle cx="7" cy="7" r="2.5" fill="#fff"/><circle cx="17" cy="7" r="2.5" fill="#fff"/><circle cx="4" cy="13" r="2.5" fill="#fff"/><circle cx="20" cy="13" r="2.5" fill="#fff"/><ellipse cx="12" cy="16" rx="5" ry="4" fill="#fff"/></svg></div>
</div>
<div class="abs card" style="left:501px">
  <div class="pic" role="img" aria-label="Photo of a puppy sitting on autumn leaves" style="background:linear-gradient(135deg,#5a3a26,#d8c8a8 55%,#7a4a2a)"></div>
  <div class="label">Potty visits</div>
  <div class="icon"><svg width="20" height="20" viewBox="0 0 24 24"><path fill="#fff" d="M4 20h16c1 0 1.5-1 1-2-1-1.5-3-2-3-2 1-1 .5-3-1-3.5.5-1.5-.5-3-2-3 0-2-2-3.5-3-4 0 2-2 3-3 4-1.5.5-2 2-1.5 3-1.5.5-2 2.5-1 3.5 0 0-2 .5-3 2-.5 1 0 2 1 2z"/></svg></div>
</div>
<div class="abs card" style="left:726px">
  <div class="pic" role="img" aria-label="Photo of dogs gathered at a grassy dog park" style="background:linear-gradient(180deg,#9cc4e8,#4f8a3a 50%,#3c6a2c)"></div>
  <div class="label">Dog park</div>
  <div class="icon"><svg width="20" height="20" viewBox="0 0 24 24"><path fill="#fff" d="M8 21v-7l-3-2 2-6 3 1 2-4 2 1v4l5 3-1 3h-3v7h-2v-5h-3v5z"/></svg></div>
</div>
<div class="abs card" style="left:948px">
  <div class="pic" role="img" aria-label="Photo of a small terrier lying on a white blanket" style="background:linear-gradient(135deg,#f1f1f1,#d8d8d8 60%,#b8a08a)"></div>
  <div class="label">MEDICATION</div>
  <div class="icon"><svg width="18" height="20" viewBox="0 0 20 24"><rect x="4" y="2" width="12" height="4" rx="1" fill="#fff"/><rect x="3" y="7" width="14" height="15" rx="2" fill="#fff"/><path d="M10 11v7M6.5 14.5h7" stroke="#1f72a8" stroke-width="2"/></svg></div>
</div>

<!-- unavailable dates -->
<div class="abs unavail"></div>
<div class="abs sec-title" style="top:1243px;color:var(--white)">Unavailable Dates</div>
<div class="abs dotted" style="top:1282px;border-color:rgba(255,255,255,.8)"></div>
<div class="abs date" style="left:398px;width:122px">May 6-8th</div>
<div class="abs date" style="left:538px;width:130px">MAY 21-23</div>
<div class="abs date" style="left:684px;width:119px">July 3-16</div>

<!-- testimonials -->
<div class="abs sec-title" style="top:1489px">What People Say</div>
<div class="abs dotted" style="top:1525px"></div>
<div class="abs quote" style="left:58px;width:404px;text-align:right">Duis aute irure dolor in reprehenderit in voluptate velit esse cillum dolore eu fugiat nulla pariatur. Excepteur sint occaecat cupidatat non proident, sunt in culpa qui officia deserunt mollit.<b>Owen Barlowe, Operations Manager</b></div>
<div class="abs avatar" style="left:489px">170x170</div>
<div class="abs vdiv"></div>
<div class="abs avatar" style="left:632px">170x170</div>
<div class="abs quote" style="left:739px;width:400px">Provident, similique sunt in culpa qui officia deserunt mollitia animi, id est laborum et dolorum fuga. Et harum quidem rerum facilis est et expedita distinctio. Nam libero tempore, cum soluta nobis.<b>Tessa Wren, Creative Designer</b></div>

<!-- photo gallery -->
<div class="abs sec-title" style="top:1731px">Photo Gallery</div>
<div class="abs dotted" style="top:1769px"></div>
<div class="abs photo" style="left:0" role="img" aria-label="Photo of a cat cuddling with a child" style="background:#5a3e2c"></div>
<div class="abs photo" style="left:0;background:linear-gradient(135deg,#3a2a22,#7a5a42 60%,#2a1e18)" role="img" aria-label="Photo of a cat cuddling with a child"></div>
<div class="abs photo" style="left:240px;background:linear-gradient(135deg,#d8cfc2,#9a5a30 50%,#f0eeea)" role="img" aria-label="Photo of a curly brown dog on a white bed"></div>
<div class="abs photo" style="left:480px;background:linear-gradient(135deg,#2a2a2a,#dcdcdc 55%,#3a3a3a)" role="img" aria-label="Photo of a black and white cat"></div>
<div class="abs photo" style="left:720px;background:linear-gradient(160deg,#6a5a50,#a06a44 55%,#c8c0b6)" role="img" aria-label="Photo of two curly puppies on a patio"></div>
<div class="abs photo" style="left:960px;background:linear-gradient(135deg,#3a2418,#a8703e 50%,#c43a32)" role="img" aria-label="Photo of a shaggy dog beside a smiling boy"></div>

<!-- footer -->
<footer class="abs footer"></footer>
<div class="abs fcol" style="left:53px">
  <h3>Contact Us</h3>
  <p>Maecenas etos sit amet, consectetur adipiscing elit. Terminal volutpat rutrum metro amet sollicitudin interdum.</p>
  <p><b>Phone:</b> +1 (555) 019 22 48</p>
  <p><b>Office:</b> 41 Larkspur Lane, Birchvale</p>
  <p><b>Email:</b> info@birchvalecritterden.com</p>
  <div class="fsocial"><span></span><span></span><span></span><span></span><span></span></div>
</div>
<div class="abs fcol" style="left:334px"><h3>Feel Free to Mail</h3></div>
<div class="field" style="top:2072px;height:31px">Name *</div>
<div class="field" style="top:2123px;height:31px">Email *</div>
<div class="field" style="top:2173px;height:51px">Write Your Message Here...</div>
<div class="abs send">SEND MESSAGE</div>
<div class="abs fcol" style="left:615px"><h3>Area Map</h3></div>
<div class="abs map" role="img" aria-label="Street map showing the office location"></div>
<div class="abs fcol" style="left:896px">
  <h3>About Team</h3>
  <p>Enim congue blandit. Lorem ipsum dolor sit amet, consectetur adipiscing elit. Quisque consectetur interdum finibus. Vestibulum ante ipsum primis in faucibus orci. luctus et ultrices posuere.</p>
  <p>Cubilia cras blandit finibus ipsum, id porttitor arcu volutpat a. Integer iaculis erat nec justo malesuada faucibus vel tempus sapien. Vivamus aliquam euismod tristique.</p>
</div>
<div class="abs fline"></div>
<div class="abs copy">Copyright 2020. All Rights Reserved</div>

</body>
</html>
```